Marlow Estates Business Card and Email Signature Design

I am a Homevant and need a business card design with my head shot picture and logo and contact information that can be prepared to be used on my email signature as well. I would like my head shot image background to match the background of the business card. So in other words the background of my head shot should be transparent. I would like the Homevant Logo on there and also PRX and Fair Dwelling Logo. My email address is: ted@marlowestates.example, Phone Number is: 555-014-7391, website: www.marlowestates.example Address: 48207 Quillfern Court Alderbrook, QX 00017
I also need just the head shot photo with white background in a JPEG file as well so I can upload that picture to my Jobtrellis and Nestavo profiles.

```html
<!DOCTYPE html>
<html lang="en">
<head>
<meta charset="utf-8">
<title>Marlow Estates Business Card</title>
<link href="https://fonts.googleapis.com/css2?family=Montserrat:wght@400;600;700&display=swap" rel="stylesheet">
<style>
  :root {
    --bg: #e9e8e6;
    --card-dark: #4a4a4a;
    --card-light: #ffffff;
    --brand-blue: #1c5582;
    --text-grey: #5e5e5e;
    --swoosh-grey: #585858;
    --white: #ffffff;
  }
  * { box-sizing: border-box; margin: 0; padding: 0; }
  html, body {
    width: 1200px; height: 930px; overflow: hidden;
    background: var(--bg);
    font-family: "Montserrat", sans-serif;
  }
  .card {
    position: absolute;
    width: 620px; height: 354px;
    border-radius: 16px;
    overflow: hidden;
    box-shadow: 0 6px 18px rgba(0,0,0,0.18);
  }
  /* front */
  .card-front { left: 290px; top: 70px; background: var(--card-dark); }
  .brand {
    position: absolute; left: 0; right: 0; top: 100px;
    display: flex; flex-direction: column; align-items: center; gap: 12px;
    color: var(--white);
  }
  .brand-dot { width: 70px; height: 70px; border-radius: 50%; background: var(--white); }
  .brand-text { display: flex; flex-direction: column; align-items: center; }
  .brand-name { font-weight: 700; font-size: 34px; letter-spacing: 1px; text-transform: uppercase; line-height: 1.1; }
  .brand-tagline { font-weight: 400; font-size: 14px; letter-spacing: 4px; text-transform: uppercase; margin-top: 4px; }

  /* back */
  .card-back { left: 290px; top: 500px; background: var(--card-light); }
  .headshot {
    position: absolute; left: 40px; top: 34px; width: 180px; height: 192px;
    border: 2px solid var(--brand-blue); padding: 6px; background: var(--card-light);
  }
  .headshot-fill {
    width: 100%; height: 100%;
    background: linear-gradient(180deg, #ffffff 0%, #f1ece8 45%, #3a3d44 100%);
  }
  .name-rule { position: absolute; left: 220px; top: 126px; width: 270px; height: 1.5px; background: var(--brand-blue); }
  .agent-name {
    position: absolute; right: 40px; top: 86px;
    font-weight: 700; font-size: 30px; color: var(--brand-blue); letter-spacing: -0.5px;
  }
  .agent-title {
    position: absolute; right: 40px; top: 122px;
    font-size: 14px; color: var(--text-grey);
  }
  .address {
    position: absolute; right: 40px; top: 166px; text-align: right;
    font-size: 15px; line-height: 1.4; color: var(--text-grey);
  }
  .contact-rule { position: absolute; left: 40px; top: 240px; width: 250px; height: 1.5px; background: var(--brand-blue); }
  .contact-list {
    position: absolute; left: 40px; top: 248px; list-style: none;
    font-size: 15px; line-height: 1.4; color: var(--text-grey);
  }
  .contact-list li { display: flex; align-items: center; gap: 10px; }
  .contact-list svg { width: 12px; height: 12px; fill: var(--brand-blue); flex: none; }
  .swoosh { position: absolute; left: 0; bottom: 0; width: 620px; height: 130px; }
</style>
</head>
<body>

<section class="card card-front">
  <div class="brand">
    <span class="brand-dot"></span>
    <div class="brand-text">
      <span class="brand-name">Marlow Estates</span>
      <span class="brand-tagline">Real Estate Services</span>
    </div>
  </div>
</section>

<section class="card card-back">
  <div class="headshot">
    <div class="headshot-fill" role="img" aria-label="Agent headshot photo"></div>
  </div>
  <div class="name-rule"></div>
  <h1 class="agent-name">TOBIAS WREN</h1>
  <p class="agent-title">Homevant</p>
  <p class="address">48207 Quillfern<br>Court Alderbrook, QX 00017</p>

  <div class="contact-rule"></div>
  <ul class="contact-list">
    <li>
      <svg viewBox="0 0 24 24"><path d="M6.6 10.8a15.1 15.1 0 0 0 6.6 6.6l2.2-2.2a1 1 0 0 1 1-.25 11.4 11.4 0 0 0 3.6.57 1 1 0 0 1 1 1V20a1 1 0 0 1-1 1A17 17 0 0 1 3 4a1 1 0 0 1 1-1h3.5a1 1 0 0 1 1 1c0 1.25.2 2.45.57 3.57a1 1 0 0 1-.25 1z"/></svg>
      555-014-7391
    </li>
    <li>
      <svg viewBox="0 0 24 24"><path d="M2 5h20v14H2zm2 2v.5l8 5 8-5V7zm0 2.8V17h16V9.8l-8 5z"/></svg>
      ted@marlowestates.example
    </li>
    <li>
      <svg viewBox="0 0 24 24"><path d="M12 2a10 10 0 1 0 0 20 10 10 0 0 0 0-20zm6.9 9h-3a15 15 0 0 0-1.3-6 8 8 0 0 1 4.3 6zM12 4.1c.9 1.3 1.7 3.6 1.9 6.9h-3.8c.2-3.3 1-5.6 1.9-6.9zM9.4 5a15 15 0 0 0-1.3 6h-3A8 8 0 0 1 9.4 5zM5.1 13h3a15 15 0 0 0 1.3 6 8 8 0 0 1-4.3-6zm6.9 6.9c-.9-1.3-1.7-3.6-1.9-6.9h3.8c-.2 3.3-1 5.6-1.9 6.9zm2.6-.9a15 15 0 0 0 1.3-6h3a8 8 0 0 1-4.3 6z"/></svg>
      www.marlowestates.example
    </li>
  </ul>

  <svg class="swoosh" viewBox="0 0 620 130" preserveAspectRatio="none">
    <path d="M0 120 L400 108 C440 106 450 78 480 60 C515 40 570 30 620 28 L620 130 L0 130 Z" fill="#585858"/>
    <path d="M0 125 L408 114 C448 112 462 84 492 68 C525 50 578 42 620 40 L620 130 L0 130 Z" fill="#ffffff"/>
    <path d="M0 129 L414 119 C455 117 470 90 500 74 C532 57 582 49 620 47 L620 130 L0 130 Z" fill="#1c5582"/>
  </svg>
</section>

</body>
</html>
```